Amber Willow Intimates

The site is an Adult Retail Store website that sells products. There will be a Splash Page and inside (Home Page). The Splash page will have normal warning to users that 18+ material is inside. The splash page will contain....

- Lady (logo)
- disclaimer link for under 18
- enter and exit buttons
- Other detail in the must have

The client has also asked that this Splash Page must set the tone for the whole site and encourage users to enter. The client would like to give a feeling of romance, beauty, elegance, classy, inviting. The client would like to move away from the stigma associated with Adult stores as “sleezy” and create a welcoming feel for both males and females.

Also an internal Home Page will be created for the website which will take the same look and feel as the Splash Page. There will be a graphic header using some of the images below. Once the Home Page has been designer there will be minor colour background changes to the internal Home Page for the 2 Shop Pages (See Below).

Amber Willow is the largest adult store in Adelaide and will be using this website primarily to sell their products online.

Target Market(s)

Described as a “his and hers adult store” Amber Willow focuses on both males and females over the age of 18.

Requirements
Must have
• Amber Willows three main colours are Black, Purple and White. Please refer to current site for exact values.
• Also various gradients of these colours are encouraged to bring the website up to date with modern trends. The current website www.amberwillowintimates-example.com.au is very outdated!
• They would like the Lady larger and on the left of the Splash Page and an Enter Site on the Splash Page. They do not like the gothic font as such however they still want a softer gothic feel and appeal. The client quite likes the use of Trajan Pro font. I have attached a concept they quite liked to give an idea of the direction they would like to head in. This is by no means a suggested look and client is open to more suggestions. They would like to see some attention paid to modifying the lady to bring it up to date.
• The client has suggested a shining moon and some stars in the background of the Splash Page. Here the “under 18” content disclaimer link needs to be put discretely down the bottom of the Splash Page. The woman’s head will eventually be a Flash file which will have her hair flowing.
• When the visitor clicks through the Enter Site they will be shown the inside Home Page of the site with a similar feel to the Splash Page and contain typical menu links such as “about us” and “contact us”. On the Home Page there will be 2 doors “His” and “Hers” where the visitor will click through to the Shop. They like the idea of open doors to enter through. Both “His” and “Hers” shop pages will have the same theme as the Home Page with a minor change in the background. Possibly a darker colour for the males side and a lighter side for the females.
• The client has hand-picked the following images from pixmarta-example.com. These may be used in the design of the Home Page at the designers discretion. Other similar images can be used to achieve the feel.
• (please search numbers at www.pixmarta-example.com for thumbnails)
• #3520947
• #6084213
• #7193052
• #8305271
• #1047389
• #2658140
• If designer can also create the Flash component there will be an extra $300 paid. Please let us know.
Nice to have
• Whilst not part of the web design component here it will be of great use if designer had flash skills. This website requires some flash animation on the logo in the Splash Page and header of the Home Page that would require woman’s hair to flow so some ongoing work could be possible for winning designer.
Should not have
• Client has made the comment that they don’t want the site to be “boring and flat”

```html
<!DOCTYPE html>
<html lang="en">
<head>
<meta charset="utf-8">
<title>Amber Willow Intimates</title>
<link rel="stylesheet" href="https://fonts.googleapis.com/css2?family=Cinzel:wght@400;700&family=Arimo:wght@400;700&display=swap">
<style>
  :root {
    --page-black: #0b0b0d;
    --plum-deep: #2c1c35;
    --plum-mid: #3f2750;
    --plum-light: #5e3b74;
    --white: #ffffff;
    --soft-white: #ece4f1;
    --moon: #f4f4f6;
    --moon-edge: #9a96a3;
    --button-edge: #e7dcef;
    --button-fill: #3a2152;
  }
  * { margin: 0; padding: 0; box-sizing: border-box; }
  html, body { width: 791px; height: 1200px; overflow: hidden; }
  body { background: var(--page-black); position: relative; font-family: "Arimo", Arial, sans-serif; color: var(--white); }

  .panel {
    position: absolute; left: 68px; width: 655px; overflow: hidden;
    background: linear-gradient(160deg, var(--plum-deep) 0%, var(--plum-mid) 55%, var(--plum-light) 100%);
  }
  .panel--splash { top: 36px; height: 491px; }
  .panel--home { top: 546px; height: 617px; }

  .logo-art {
    position: absolute; border-radius: 50%;
    background: radial-gradient(circle at 50% 45%, var(--moon) 0%, #d9d8dd 45%, var(--moon-edge) 62%, rgba(154,150,163,0) 72%);
  }
  .panel--splash .logo-art { left: -10px; top: 50px; width: 260px; height: 360px; }
  .panel--home .logo-art { left: 105px; top: 12px; width: 145px; height: 185px; }

  .brand-name { position: absolute; font-family: "Cinzel", "Trajan Pro", serif; font-weight: 400; color: var(--soft-white); text-align: center; line-height: 1; }
  .brand-name span { display: block; }
  .panel--splash .brand-name { left: 245px; width: 385px; top: 106px; }
  .panel--splash .brand-name .line-top { font-size: 36px; }
  .panel--splash .brand-name .line-bottom { font-size: 52px; margin-top: 16px; }
  .panel--home .brand-name { left: 255px; width: 290px; top: 48px; }
  .panel--home .brand-name .line-top { font-size: 27px; }
  .panel--home .brand-name .line-bottom { font-size: 38px; margin-top: 12px; }

  .site-choice { position: absolute; top: 286px; font-family: "Cinzel", serif; font-size: 14px; letter-spacing: 0.5px; color: var(--soft-white); text-decoration: none; }
  .site-choice--leave { left: 301px; }
  .site-choice--enter { left: 496px; }

  .disclaimer { position: absolute; font-size: 8.4px; line-height: 10px; letter-spacing: 0.2px; color: var(--soft-white); }
  .panel--splash .disclaimer { left: 238px; width: 400px; top: 357px; text-align: center; }
  .popup-note { position: absolute; left: 238px; width: 400px; top: 386px; text-align: center; font-size: 6px; color: var(--soft-white); }
  .plugin-mark { position: absolute; left: 432px; top: 403px; width: 14px; height: 14px; border-radius: 50%; border: 1.5px solid var(--white); }

  .hero-photo {
    position: absolute; left: 0; top: 280px; width: 270px; height: 265px;
    background: radial-gradient(ellipse at 45% 45%, rgba(150,125,160,0.55) 0%, rgba(110,85,125,0.35) 45%, rgba(60,40,75,0) 75%);
  }

  .main-nav { position: absolute; left: 68px; top: 212px; list-style: none; }
  .main-nav li { font-family: "Cinzel", serif; font-size: 11.5px; height: 26px; color: var(--soft-white); }

  .welcome { position: absolute; left: 238px; top: 212px; width: 380px; font-size: 10px; line-height: 12px; color: var(--white); }
  .welcome p { margin-bottom: 12px; }
  .product-list { list-style: none; margin-bottom: 12px; }

  .shop-door {
    position: absolute; top: 460px; width: 87px; height: 56px; border-radius: 6px;
    border: 1px solid var(--button-edge);
    background: linear-gradient(180deg, #7b5a93 0%, var(--button-fill) 50%, #2a153d 100%);
    box-shadow: 0 0 8px rgba(210,180,235,0.6);
    font-family: "Cinzel", serif; font-size: 26px; color: var(--white);
    display: flex; align-items: center; justify-content: center; text-decoration: none;
  }
  .shop-door--his { left: 300px; }
  .shop-door--her { left: 435px; }

  .site-footer { position: absolute; right: 11px; top: 565px; text-align: right; }
  .site-footer .disclaimer { position: static; font-size: 7.4px; line-height: 9px; }
  .copyright { margin-top: 6px; font-size: 7.4px; color: var(--soft-white); }
  .copyright strong { font-weight: 700; }
</style>
</head>
<body>

<section class="panel panel--splash">
  <div class="logo-art" role="img" aria-label="Silhouette of a woman with a whip before a shining moon, clouds and stars"></div>
  <h1 class="brand-name"><span class="line-top">AMBER WILLOW</span><span class="line-bottom">INTIMATES</span></h1>
  <a class="site-choice site-choice--leave" href="#">LEAVE SITE</a>
  <a class="site-choice site-choice--enter" href="#">ENTER SITE</a>
  <p class="disclaimer">Contents of this website may contain explicit materials which may offend some people.<br>This website is designed for Mature Audiences 18+</p>
  <p class="popup-note">please disable any pop up blockers</p>
  <span class="plugin-mark"></span>
</section>

<section class="panel panel--home">
  <div class="hero-photo" role="img" aria-label="Faded romantic photo of an embracing couple"></div>
  <div class="logo-art" role="img" aria-label="Silhouette of a woman with a whip before a shining moon, clouds and stars"></div>
  <h2 class="brand-name"><span class="line-top">AMBER WILLOW</span><span class="line-bottom">INTIMATES</span></h2>

  <ul class="main-nav">
    <li>HOME</li>
    <li>ABOUT US</li>
    <li>OUR SHOP</li>
    <li>CONTACT US</li>
  </ul>

  <div class="welcome">
    <p>Welcome to our business - Amber Willow Intimates His &amp; Hers Adult Shop</p>
    <p>Amber Willow Intimates was established in 1985 at Harlow Vale and established at Ferncliff in 2003.</p>
    <p>We have worked very hard to make our adult shops the one stop adult shop by keeping the biggest selection of adult products:</p>
    <ul class="product-list">
      <li>- Toys for women and men - Lingerie</li>
      <li>- Education DVDs, videos, books - Shoes</li>
      <li>- Contact mags - Leather</li>
      <li>- Magazines (softcore &amp; hardcore) - Bondage</li>
      <li>- Novels - Lubes, lotions, massage oils &amp; sprays</li>
      <li>- Adult games - Pills for men &amp; women</li>
      <li>- Body jewellery - Condoms</li>
      <li>- Latex for men &amp; women</li>
    </ul>
    <p>We have a large range of DVDs, videos and novelties for all occasions so don't hesitate to come in and see us or call our friendly staff for more information.</p>
  </div>

  <a class="shop-door shop-door--his" href="#">HIS</a>
  <a class="shop-door shop-door--her" href="#">HER</a>

  <footer class="site-footer">
    <p class="disclaimer">Contents of this website may contain explicit materials which may offend some people.<br>This website is designed for Mature Audiences 18+</p>
    <p class="copyright">© 2010 Amber Willow Intimates &nbsp;|&nbsp; <strong>All Rights Reserved</strong></p>
  </footer>
</section>

</body>
</html>
```